Marisol Penhaw tutoring Advertising package - flyers, posters, business card and logo

I am looking for a flyer design for my tutoring business, it needs to explain what tutoring services I offer, how much I charge, why my services are worthwhile, it should include some photos of me and the tutoring centre,

It needs to include my phone number and my website. It should quote from some of the testimonials I have received from parents and children.

My website is www.marisolpenhaw.example My Facebook page can be found at https://www.facebook.example/marisolpenhawtutoring These pages include a range of photos and quotes that you can use.

I am not sure about the colours and designs that I would like, that's why I'm using Artflock!
I'm looking to appeal to parents inform them of my skills and experience.

I'm charging $45 for sessions of an hour and 15 minutes. 2 sessions per week will cost $80. I tutor Monday to Friday afternoons and evenings along with all day Saturdays. The assessment is free.

I tutor children from K-9 in English and Maths. I'm mainly aiming at parents whose children are struggling a little bit at school although I can help children who are doing well too.
I am highly skilled at helping children who can't read, I have a comprehensive program, the Calder program, that specifically teaches children the skills they need to read fluently and successfully.

Similarly I have had a lot of experience at helping children improve their Maths skills. I am well resourced with a wide range of hands on resources, paper resources and electronic resources.

Children will get better NAPLAN results if I tutor them (NAPLAN is the national series of tests in Australia).

I'm after a DL double sided flyer, and an A4 flyer. I'm also looking for two A2 posters and two A3 posters. Finally, I want a business card too. I don't have a logo for the business and I'd love to have one!

Target Market(s)

Parents of school aged children

Industry/Entity Type

Education

Colors

Designer to choose colors to be used in the design.

Requirements
Must have
• my name, my photo, length and cost of my sessions, email and phone contact details. Subjects and age ranges that I teach, times that I tutor. Website and/or Facebook page references. Quotes from Testimonials
Nice to have
• The A2 and A3 posters should complement each other.

```html
<!DOCTYPE html>
<html lang="en">
<head>
<meta charset="utf-8">
<title>Marisol Penhaw Tutoring – A4 Flyer</title>
<link rel="stylesheet" href="https://fonts.googleapis.com/css2?family=Nunito+Sans:wght@300;400;700;800;900&family=Oswald:wght@500&display=swap">
<style>
  :root {
    --stage: #6f6f6f;
    --paper: #ffffff;
    --ink: #111111;
    --sky: #3f80c2;
    --teal: #22b39a;
    --navy: #34508f;
    --lime: #8cc63f;
    --tick: #f4e11c;
    --link-blue: #3f6fae;
  }
  * { box-sizing: border-box; margin: 0; padding: 0; }
  html, body { width: 945px; height: 1200px; overflow: hidden; }
  body {
    background: var(--stage);
    font-family: "Nunito Sans", Arial, sans-serif;
    position: relative;
  }
  .flyer {
    position: absolute; left: 80px; top: 92px;
    width: 785px; height: 1016px;
    background: var(--paper); overflow: hidden;
  }
  .abs { position: absolute; }

  /* top services row */
  .services { left: 0; top: 18px; width: 785px; display: flex; justify-content: center; }
  .services li {
    list-style: none; text-align: center; font-weight: 800; font-size: 16px;
    line-height: 19px; color: var(--ink); padding: 0 22px;
  }
  .services li + li { border-left: 4px solid var(--teal); }

  /* wordmark */
  .wordmark { left: 340px; top: 78px; display: flex; align-items: center; gap: 22px; }
  .wordmark-square { width: 64px; height: 64px; background: var(--sky); }
  .wordmark-name {
    color: var(--sky); font-weight: 800; font-size: 29px; line-height: 33px; letter-spacing: .3px;
  }

  /* bands */
  .band-hero { left: 0; top: 186px; width: 785px; height: 342px; background: var(--sky); }
  .band-pricing { left: 0; top: 528px; width: 785px; height: 178px; background: var(--teal); }
  .band-voices { left: 0; top: 706px; width: 785px; height: 224px; background: var(--navy); }

  .hero-photo {
    left: 0; top: 103px; width: 290px; height: 425px;
    background: linear-gradient(160deg, #f1d7c6 0%, #c94c4c 55%, #7a3a3a 100%);
  }

  .hero-title {
    left: 312px; top: 214px; color: #fff; font-weight: 800; font-size: 31px; line-height: 36px;
  }
  .benefits { left: 522px; top: 203px; width: 250px; list-style: none; }
  .benefits li {
    position: relative; padding-left: 22px; color: #fff; font-weight: 700;
    font-size: 14.5px; line-height: 17px; margin-bottom: 8px;
  }
  .benefits svg { position: absolute; left: 0; top: 3px; }

  .slogan { left: 370px; top: 408px; width: 390px; text-align: center; color: #fff; }
  .slogan-soft { font-weight: 300; font-size: 27px; line-height: 32px; letter-spacing: .5px; }
  .slogan-strong { font-weight: 900; font-size: 41px; line-height: 46px; }

  /* pricing */
  .pricing { left: 38px; top: 543px; color: #fff; }
  .price { font-weight: 900; font-size: 22px; line-height: 24px; }
  .price-note { font-size: 12px; line-height: 14px; margin-bottom: 14px; }
  .hours { font-weight: 800; font-size: 13px; line-height: 17px; margin-top: 10px; }

  .photo-frame { top: 544px; width: 209px; height: 147px; background: #fff; padding: 5px; }
  .photo-frame .fill { width: 100%; height: 100%; }
  .frame-centre { left: 304px; }
  .frame-tutor { left: 534px; }
  .fill-centre { background: linear-gradient(180deg, #8a6d4c 0%, #c9b18a 55%, #7a4a28 100%); }
  .fill-tutor { background: linear-gradient(180deg, #e3dccb 0%, #9ab0c6 50%, #6b3e20 100%); }

  /* testimonials */
  .voices-heading {
    left: 0; top: 723px; width: 785px; text-align: center; color: #fff;
    font-weight: 800; font-size: 20px; line-height: 24px;
  }
  .voices-heading span { color: var(--lime); }
  .quote { top: 762px; color: #fff; font-size: 11.5px; line-height: 14.2px; }
  .quote cite { display: block; text-align: right; font-style: normal; font-weight: 800; margin-top: 2px; }
  .q1 { left: 43px; width: 190px; }
  .q2 { left: 263px; width: 210px; }
  .q3 { left: 505px; width: 240px; top: 759px; }

  /* footer */
  .free-badge {
    left: 38px; top: 924px; width: 237px; height: 36px; background: var(--teal);
    color: #fff; font-family: "Oswald", "Arial Narrow", sans-serif; font-weight: 500;
    font-size: 23px; line-height: 36px; text-align: center;
  }
  .contact-cta {
    left: 38px; top: 966px; width: 237px; text-align: center; color: var(--link-blue);
    font-weight: 800; font-size: 19px;
  }
  .phone { left: 296px; top: 942px; display: flex; align-items: center; gap: 10px;
    color: var(--teal); font-weight: 900; font-size: 32px; line-height: 36px; }
  .website { left: 296px; top: 982px; width: 264px; text-align: center;
    color: var(--link-blue); font-weight: 700; font-size: 15px; }
  .address { left: 582px; top: 947px; width: 196px; font-style: normal;
    font-size: 12.5px; line-height: 16px; color: var(--ink); }
  .address p { position: relative; padding-left: 16px; white-space: nowrap; }
  .address p + p { margin-top: 12px; }
  .address svg { position: absolute; left: 0; top: 2px; }
</style>
</head>
<body>
<main class="flyer">
  <ul class="services abs">
    <li>Grades<br>from K-9</li>
    <li>Maths English and<br>Maths Enrichments</li>
    <li>Homework Help<br>School Test Prep</li>
    <li>Algebra / Trig<br>Calculus / Geometry</li>
  </ul>

  <div class="wordmark abs">
    <div class="wordmark-square"></div>
    <div class="wordmark-name">MARISOL PENHAW<br>TUTORING</div>
  </div>

  <section class="band-hero abs"></section>
  <div class="hero-photo abs" role="img" aria-label="Smiling schoolgirl in a tartan uniform with a backpack giving a thumbs up"></div>

  <h1 class="hero-title abs">Tutoring<br>That works</h1>
  <ul class="benefits abs">
    <li><svg width="14" height="11" viewBox="0 0 14 11"><path d="M1 5.5l4 4L13 1" fill="none" stroke="#f4e11c" stroke-width="3"/></svg>Calder program to help your child read.</li>
    <li><svg width="14" height="11" viewBox="0 0 14 11"><path d="M1 5.5l4 4L13 1" fill="none" stroke="#f4e11c" stroke-width="3"/></svg>Focus on Specific learning areas</li>
    <li><svg width="14" height="11" viewBox="0 0 14 11"><path d="M1 5.5l4 4L13 1" fill="none" stroke="#f4e11c" stroke-width="3"/></svg>Individual Program design</li>
    <li><svg width="14" height="11" viewBox="0 0 14 11"><path d="M1 5.5l4 4L13 1" fill="none" stroke="#f4e11c" stroke-width="3"/></svg>Reading, writing, spelling, grammer and maths</li>
    <li><svg width="14" height="11" viewBox="0 0 14 11"><path d="M1 5.5l4 4L13 1" fill="none" stroke="#f4e11c" stroke-width="3"/></svg>Positive and supportive learning environment designed to promote confidence</li>
  </ul>

  <div class="slogan abs">
    <div class="slogan-soft">MAKE THIS SCHOOL YEAR</div>
    <div class="slogan-strong">GREATER THAN</div>
    <div class="slogan-soft">LAST YEAR....</div>
  </div>

  <section class="band-pricing abs"></section>
  <div class="pricing abs">
    <div class="price">$45 PER SESSION</div>
    <div class="price-note">(one hour and 15 minutes)</div>
    <div class="price">$80 TWO SESSIONS</div>
    <div class="price-note">per week</div>
    <div class="hours">Monday to Friday afternoons and<br>evenings along with all day Saturdays.</div>
  </div>
  <figure class="photo-frame frame-centre abs"><div class="fill fill-centre" role="img" aria-label="Tutoring centre room with bookshelves and a wooden table"></div></figure>
  <figure class="photo-frame frame-tutor abs"><div class="fill fill-tutor" role="img" aria-label="The tutor seated at a desk in the tutoring room"></div></figure>

  <section class="band-voices abs"></section>
  <h2 class="voices-heading abs">WHAT PARENTS ARE SAYING ABOUT <span>MARISOL PENHAW TUTORING</span></h2>
  <blockquote class="quote q1 abs">Our son has been tutored by Marisol now for the past 2 years - we have noticed a big improvement with his spelling and mathematics. This has also helped our son's confidence in his daily schooling and he now has started to enjoy school again . Thanks Marisol<cite>Owen and Tessa Marlowe</cite></blockquote>
  <blockquote class="quote q2 abs">Our children love going to Marisol's!! Yes you read that right - they LOVE going to learn! Marisol has the ability to tap into each child's strengths and weaknesses and makes learning fun! Our children's grades have improved more so, our son just got awarded a distinction in a science competition! Thanks so much Marisol<cite>Fiona Keel</cite></blockquote>
  <blockquote class="quote q3 abs">My daughter has been seeing Marisol for about a year now. The improvement in her reading and writing is amazing. She has gone from getting 2s on her report cards to getting 4s. I'm always telling people Marisol is one of those people who you just have a conversation with and you learn something. I plan to start tutoring for my 2 boys with Marisol asap. She is always friendly and understanding of life's circumstances.<cite>Dana Whitcombe</cite></blockquote>

  <div class="free-badge abs">ASSESSMENT IS FREE</div>
  <div class="contact-cta abs">CONTACT ME TODAY!</div>
  <div class="phone abs">
    <svg width="28" height="22" viewBox="0 0 28 22"><path d="M2 8c0-4 5-6 12-6s12 2 12 6v2h-7V7c-3-1-7-1-10 0v3H2zM6 12h16l3 8H3z" fill="#22b39a"/></svg>
    <span>0400 555 183</span>
  </div>
  <div class="website abs">www.marisolpenhaw.example</div>
  <address class="address abs">
    <p><svg width="9" height="12" viewBox="0 0 9 12"><path d="M4.5 0A4.5 4.5 0 0 0 0 4.5C0 8 4.5 12 4.5 12S9 8 9 4.5A4.5 4.5 0 0 0 4.5 0zm0 6.2a1.7 1.7 0 1 1 0-3.4 1.7 1.7 0 0 1 0 3.4z" fill="#3f80c2"/></svg>14 Wattle Crt Brenfield<br>NSW 2199.</p>
    <p><svg width="10" height="8" viewBox="0 0 10 8"><rect width="10" height="8" rx="1" fill="#3f80c2"/><path d="M0 1l5 3.5L10 1" fill="none" stroke="#fff" stroke-width="1"/></svg>marisolpenhaw@mail.example</p>
  </address>
</main>
</body>
</html>
```